Wine Bottle Label for Tall Fern Cellars

We are a small, newly established winery in need of an original, bold and outstanding bottle label design for our Tall Fern wine.

Our vineyard and winery are located on a 200 acre farm in a remote part of southern Oregon. The name "Tall Fern" was inspired by the large, overgrown size of all of the foliage here, including our grapevines. Things grow large and vigorous in Oregon! And everything is very lush and green. It is almost surreal or other-worldly, like the landscapes seen in the Keeper of The Stones movies, or the land of Quill. It is a place that makes you say "wow" with its epic, large scale, natural beauty.

The name "Tall Fern" also captures the essence of our wine. It is big in flavor, quality and color. Our first release is a Pinot Noir (red). Pinot Noir wines often are subtle in flavor and thin in their color. Our label should convey that our Pinot Noir is a much more robust, darker, heavier, meatier, more flavorful wine that is a lot more fun than an "ordinary" wine. At the same time, this wine is not cheap, and so nothing in the label should convey "bargain," "low price," or "cheapness." This is a fine wine with a sense of adventure. Be sure to convey "quality" with your design along with "big," "adventure" and "fun".

The label should appeal to a younger demographic, both male and female, between the ages of 21 and 35. It should be non-traditional and adventurous and suggest a pushing of boundaries and a breaking of rules. This Pinot Noir does not conform to the normal "limitations" of the variety, therefore the label should not conform. It should have an "organic" or "natural" or "agricultural" vibe, as opposed to something mechanical or technical. It should, however, be contemporary. Do not confuse "natural" or "organic" with being nostalgic or old school. Think "agri-hipsters."

The label should be designed to fit on a Burgundy-style wine bottle (photo attached for reference). (Note: All Pinot Noir and Chardonnay is bottled in Burgundy bottles, If you are not sure about the bottle shape you can go to a local store and compare the various bottles. Locate a bottle of Pinot Noir or Chardonnay or anything identified as a "Burgundy Wine," and it should be the correct bottle. The tall, skinny bottles used for Cabernet Sauvignon are NOT correct)). Please see the "Must Have" notes for more on the bottle.

In summary, the final project should be a wine bottle label design that conveys bigness, vastness, adventurous, non-traditional, high quality wine. A good tagline to keep in mind is "Living Large."

Target Market(s)

Young, hip, non-conformist wine drinkers aged 21-35 with a sense of adventure and an appreciation of quality.

Requirements
Must have
• *Must contain the words:

Tall Fern (the brand)
2013 Pinot Noir (the vintage year and variety)

*The label must be designed to fit a Burgundy-style wine bottle. A photo is attached for reference.

*Additionally, the label needs to fit on the lower, widest part of the bottle. The label will be printed on sticky paper and rolled onto the bottle with a machine. The machine cannot apply labels to the neck of the bottle. The maximum size of a label that will fit this space is 5.5 inches wide by 4.5 inches tall. You DO NOT have to fill ALL of this space or confine the label shape to a rectangle, but the label cannot exceed this size or it won't stick to the bottle properly. It will really help if you can put your hands on an actual bottle to see the logistics of applying the label. But if that is not possible, just do your best with the instructions you have. I am confident the winning design could be adjusted to fit the bottle, if necessary
Nice to have
• *Wine grape leaf or leaves.

*A concept I have been playing with is sunlight shining through leaves like light through a Harwick lamp or a stained glass window. This is NOT a requirement for this label. However, if the concept inspires and idea, I would be most happy to see it.
Should not have
• IF a leaf or leaves are included in the design (not a requirement) they MUST be wine grapevine leafs and preferably leaves of the Pinot Noir vine. Do not use generic leaves or identifiable leaves such as oak leaves, maple leaves, or anything that looks like the Canadian flag or the Duluth Granite Hawks hockey logo. Reference the attached photos of wine grape leaves to see the correct leaf type. I am happy to email more photos upon request. These photos may be used in whole or in part in your design, however, a leaf from a photo is NOT a requirement, nor is the image of a leaf or leaves.

This label should NOT be designed for Bordeaux-style wine bottles (the tall, skinny ones).

```html
<!DOCTYPE html>
<html lang="en">
<head>
<meta charset="UTF-8">
<title>Tall Fern Pinot Noir Label</title>
<link rel="stylesheet" href="https://fonts.googleapis.com/css2?family=Libre+Baskerville&family=Cormorant+Garamond:ital,wght@1,500&family=Roboto:wght@400&display=swap">
<style>
  :root {
    --page: #ffffff;
    --label-black: #0b0a0c;
    --grape-deep: #120a1e;
    --grape-mid: #33205a;
    --grape-light: #4e3585;
    --gold: #d2b25a;
    --gold-muted: #b39548;
    --white: #f4f1ea;
  }
  html, body {
    margin: 0;
    width: 1200px;
    height: 900px;
    overflow: hidden;
    background: var(--page);
  }
  .canvas {
    position: relative;
    width: 1200px;
    height: 900px;
  }
  .wine-label {
    position: absolute;
    left: 368px;
    top: 98px;
    width: 464px;
    height: 704px;
  }
  .label-shape {
    position: absolute;
    inset: 0;
  }
  .label-text {
    position: absolute;
    left: 0;
    width: 464px;
    margin: 0;
    text-align: center;
    white-space: nowrap;
    line-height: 1;
  }
  .brand-name {
    top: 243px;
    font-family: "Libre Baskerville", serif;
    font-weight: 400;
    font-size: 66px;
    color: var(--gold);
  }
  .variety {
    top: 400px;
    font-family: "Libre Baskerville", serif;
    font-size: 36px;
    color: var(--gold-muted);
  }
  .vintage {
    top: 503px;
    font-family: "Libre Baskerville", serif;
    font-size: 34px;
    color: var(--white);
  }
  .origin {
    top: 556px;
    font-family: "Cormorant Garamond", serif;
    font-style: italic;
    font-weight: 500;
    font-size: 32px;
    line-height: 38px;
    color: var(--gold-muted);
  }
  .fine-print {
    position: absolute;
    top: 680px;
    margin: 0;
    font-family: "Roboto", sans-serif;
    font-size: 12px;
    line-height: 1;
    letter-spacing: 0.5px;
    color: var(--gold-muted);
  }
  .fine-print.alcohol { left: 10px; }
  .fine-print.volume { right: 14px; }
</style>
</head>
<body>
<main class="canvas">
  <section class="wine-label">
    <svg class="label-shape" width="464" height="704" viewBox="0 0 464 704">
      <defs>
        <clipPath id="label-outline">
          <path d="M0,696 V182 Q0,172 12,172 C20,128 50,116 70,128 C70,70 110,46 135,68 C130,24 175,0 200,22 C220,0 260,10 262,38 C285,12 330,22 325,62 C345,46 370,50 372,78 C395,68 410,96 400,118 C425,108 450,124 440,158 C455,158 464,170 464,182 V696 Q464,704 456,704 H8 Q0,704 0,696 Z"/>
        </clipPath>
        <radialGradient id="grape-tones" cx="0.55" cy="0.35" r="0.75">
          <stop offset="0" stop-color="var(--grape-light)"/>
          <stop offset="0.45" stop-color="var(--grape-mid)"/>
          <stop offset="1" stop-color="var(--grape-deep)"/>
        </radialGradient>
      </defs>
      <g clip-path="url(#label-outline)">
        <rect class="grape-cluster" x="0" y="0" width="464" height="496" fill="url(#grape-tones)" role="img" aria-label="Photograph of a dark purple Pinot Noir grape cluster"/>
        <rect class="lower-band" x="0" y="496" width="464" height="208" fill="var(--label-black)"/>
      </g>
      <line class="vintage-rule" x1="8" y1="520" x2="172" y2="520" stroke="var(--gold)" stroke-width="2"/>
      <line class="vintage-rule" x1="292" y1="520" x2="456" y2="520" stroke="var(--gold)" stroke-width="2"/>
    </svg>
    <h1 class="label-text brand-name">Tall Fern</h1>
    <p class="label-text variety">Pinot Noir</p>
    <p class="label-text vintage">2013</p>
    <p class="label-text origin">Product of<br>Southern Oregon</p>
    <p class="fine-print alcohol">ALCOHOL 13.5% BY VOLUME</p>
    <p class="fine-print volume">750ML</p>
  </section>
</main>
</body>
</html>
```